The Quiet Hinge Mending Ledger

I am making a journal for tracking pain symptoms for TMJ (Jaw) pain. I have the cover designed and I just need the journal page designed that will repeat throughout the journal. The journal is the image on the left of the bundle. The page I would like to be developed is the picture that I hand sketched out. It should be a 6 x 9 page, similar to the attached example. Greyscale, no color. Thank you!

Target Market(s)

20-55 year old women

Industry/Entity Type

Healthcare

Colors

Designer to choose only greyscale colors for use in the design.

Requirements
Must have
• A neat, well-designed page with the content I have sketched out by hand.
Nice to have
• Creative display of the content I provided and development of the pain scale and pain diagram faces in a professional looking way.

```html
<!DOCTYPE html>
<html lang="en">
<head>
<meta charset="utf-8">
<title>The Quiet Hinge Mending Ledger – Daily Page</title>
<link href="https://fonts.googleapis.com/css2?family=Raleway:wght@400;700&family=Open+Sans:wght@400;700&display=swap" rel="stylesheet">
<style>
  :root {
    --backdrop: #f1f1f1;
    --paper: #ffffff;
    --bar: #b0b0b0;
    --bar-text: #ffffff;
    --row-light: #d6d6d6;
    --row-dark: #bdbdbd;
    --rule: #ffffff;
    --box: #d6d6d6;
    --soft-text: #a6a6a6;
    --ink: #111111;
    --line: #b5b5b5;
    --art-top: #8a8a8a;
    --art-bottom: #e6e6e6;
  }
  * { margin: 0; padding: 0; box-sizing: border-box; }
  html, body { width: 900px; height: 1200px; overflow: hidden; }
  body { background: var(--backdrop); font-family: "Raleway", Arial, sans-serif; }
  .canvas { position: relative; width: 900px; height: 1200px; }
  .page { position: absolute; left: 87px; top: 55px; width: 726px; height: 1090px; background: var(--paper); }
  .abs { position: absolute; }

  .bar { position: absolute; background: var(--bar); color: var(--bar-text); font-weight: 700; font-size: 13.5px; height: 26px; line-height: 26px; letter-spacing: .2px; }
  .bar.center { text-align: center; left: 124px; width: 651px; }
  .bar.left { padding-left: 12px; }
  .bar.small { height: 24px; line-height: 24px; }

  .log-table { position: absolute; top: 137px; border-collapse: collapse; font-size: 13.5px; }
  .log-table th { background: var(--bar); color: var(--bar-text); font-weight: 700; height: 27px; border-left: 1px solid var(--rule); }
  .log-table th:first-child { border-left: none; }
  .log-table td { height: 27px; border-left: 1px solid var(--rule); }
  .log-table td.num { color: var(--bar-text); text-align: center; border-left: none; font-size: 13px; }
  .log-table tr:nth-child(odd) td { background: var(--row-light); }
  .log-table tr:nth-child(even) td { background: var(--row-dark); }
  .col-num { width: 34px; } .col-time { width: 83px; }

  .check { position: absolute; display: flex; align-items: center; gap: 6px; color: var(--soft-text); font-size: 13.5px; white-space: nowrap; }
  .check::before { content: ""; width: 16px; height: 16px; background: var(--box); flex: none; }

  .scale .check { top: 323px; font-size: 13px; }

  .faces { position: absolute; top: 393px; left: 124px; width: 651px; height: 225px; display: flex; }
  .face { position: relative; border-left: 1.5px solid var(--ink); text-align: center; display: flex; flex-direction: column; align-items: center; }
  .face:first-child { border-left: none; }
  .face-art { width: 82px; height: 112px; margin-top: 8px; border-radius: 40px 40px 30px 30px; background: linear-gradient(180deg, var(--art-top), var(--art-bottom)); }
  .face-name { font-family: "Open Sans", Arial, sans-serif; font-weight: 700; font-size: 13.5px; color: var(--ink); margin-top: 9px; }
  .face-desc { font-family: "Open Sans", Arial, sans-serif; font-size: 11px; line-height: 15px; color: var(--ink); }

  .write-line { position: absolute; height: 1.5px; background: var(--line); }
</style>
</head>
<body>
<div class="canvas">
  <div class="page"></div>

  <div class="bar left small" style="left:124px;top:85px;width:223px;">DATE</div>
  <div class="bar left small" style="left:478px;top:85px;width:297px;">DAY OF THE WEEK</div>

  <table class="log-table" style="left:124px;">
    <tr><th class="col-num"></th><th class="col-time">BEGIN</th><th class="col-time">END</th><th style="width:98px;">DURATION</th></tr>
    <tr><td class="num">1</td><td></td><td></td><td></td></tr>
    <tr><td class="num">2</td><td></td><td></td><td></td></tr>
    <tr><td class="num">3</td><td></td><td></td><td></td></tr>
    <tr><td class="num">4</td><td></td><td></td><td></td></tr>
  </table>
  <table class="log-table" style="left:478px;">
    <tr><th class="col-num"></th><th class="col-time">BEGIN</th><th class="col-time">END</th><th style="width:98px;">DURATION</th></tr>
    <tr><td class="num">1</td><td></td><td></td><td></td></tr>
    <tr><td class="num">2</td><td></td><td></td><td></td></tr>
    <tr><td class="num">3</td><td></td><td></td><td></td></tr>
    <tr><td class="num">4</td><td></td><td></td><td></td></tr>
  </table>

  <div class="bar center" style="top:287px;">SEVERITY OF PAIN (CIRCLE RANGE)</div>
  <div class="scale">
    <span class="check" style="left:124px;">1</span>
    <span class="check" style="left:189px;">2</span>
    <span class="check" style="left:258px;">3</span>
    <span class="check" style="left:327px;">4</span>
    <span class="check" style="left:395px;">5</span>
    <span class="check" style="left:464px;">6</span>
    <span class="check" style="left:533px;">7</span>
    <span class="check" style="left:601px;">8</span>
    <span class="check" style="left:670px;">9</span>
    <span class="check" style="left:739px;">10</span>
  </div>

  <div class="bar center" style="top:356px;">LOCATION</div>
  <div class="faces">
    <div class="face" style="width:114px;">
      <div class="face-art" role="img" aria-label="Drawing of a woman in profile with shading at the temple in front of the ear"></div>
      <div class="face-name">TMJ</div>
      <div class="face-desc">pain is at<br>temples,<br>in front<br>of ears.</div>
    </div>
    <div class="face" style="width:103px;">
      <div class="face-art" role="img" aria-label="Drawing of a man's head with shading over browbones and cheekbones"></div>
      <div class="face-name">Sinus</div>
      <div class="face-desc">pain is<br>behind<br>browbone<br>and/or<br>cheekbone.</div>
    </div>
    <div class="face" style="width:112px;">
      <div class="face-art" role="img" aria-label="Drawing of a man's head with shading around one eye"></div>
      <div class="face-name">Cluster</div>
      <div class="face-desc">pain is<br>in and<br>around<br>one eye.</div>
    </div>
    <div class="face" style="width:112px;">
      <div class="face-art" role="img" aria-label="Drawing of a woman's head with a shaded band across the forehead"></div>
      <div class="face-name">Tension</div>
      <div class="face-desc">pain is<br>like a<br>band<br>squeezing<br>the head.</div>
    </div>
    <div class="face" style="width:109px;">
      <div class="face-art" role="img" aria-label="Drawing of a man's head with one half shaded"></div>
      <div class="face-name">Migraine</div>
      <div class="face-desc">pain, nausea<br>and visual<br>changes are<br>typical of<br>classic form.</div>
    </div>
    <div class="face" style="width:101px;">
      <div class="face-art" role="img" aria-label="Drawing of a man in profile with shading at the top and back of the head"></div>
      <div class="face-name">Neck</div>
      <div class="face-desc">pain is at<br>the top<br>and/or<br>back of head.</div>
    </div>
  </div>

  <div class="bar center" style="top:636px;">TRIGGERS (CHECK ALL THAT APPLY)</div>
  <span class="check" style="left:124px;top:674px;">Sleep</span>
  <span class="check" style="left:124px;top:701px;">My First Thing in AM</span>
  <span class="check" style="left:124px;top:728px;">Clenching</span>
  <span class="check" style="left:333px;top:674px;">Insomnia</span>
  <span class="check" style="left:333px;top:701px;">Eating</span>
  <span class="check" style="left:333px;top:728px;">Work</span>
  <span class="check" style="left:467px;top:674px;">Yawn</span>
  <span class="check" style="left:467px;top:701px;">PMS/ Menstration</span>
  <span class="check" style="left:467px;top:728px;">Stress at Home</span>
  <span class="check" style="left:659px;top:674px;">Stress at Work</span>
  <span class="check" style="left:659px;top:701px;">Weather</span>
  <span class="check" style="left:659px;top:728px;">Other</span>

  <div class="bar" style="left:124px;top:767px;width:155px;text-align:center;">MY SAWS WAS</div>
  <span class="check" style="left:289px;top:772px;">Clenched</span>
  <span class="check" style="left:395px;top:772px;">Relaxed</span>
  <div class="bar" style="left:124px;top:805px;width:155px;text-align:center;">MY BREATH WAS</div>
  <span class="check" style="left:289px;top:810px;">Shallow</span>
  <span class="check" style="left:395px;top:810px;">Relaxed</span>
  <div class="bar" style="left:512px;top:767px;width:256px;text-align:center;">MY NECK/ SHOULDERS WERE</div>
  <span class="check" style="left:512px;top:802px;">Tense</span>
  <span class="check" style="left:619px;top:802px;">Relaxed</span>

  <div class="bar center" style="top:856px;">RELIEF MEASURES (CHECK ALL THAT APPLY)</div>
  <span class="check" style="left:124px;top:891px;">Deep Breathing</span>
  <span class="check" style="left:124px;top:918px;">Teeth apart/ Relax jaw</span>
  <span class="check" style="left:124px;top:945px;">Self Massage</span>
  <span class="check" style="left:124px;top:972px;">Stabilization Exercise</span>
  <span class="check" style="left:413px;top:891px;">Heat/ Cold</span>
  <span class="check" style="left:413px;top:918px;">Medication</span>
  <span class="check" style="left:413px;top:945px;">Rest</span>
  <span class="check" style="left:413px;top:972px;">Others</span>
  <div class="write-line" style="left:489px;top:985px;width:286px;"></div>
  <span class="check" style="left:629px;top:891px;">Gentle Stretching</span>
  <span class="check" style="left:629px;top:918px;">Posture Correction</span>
  <span class="check" style="left:629px;top:945px;">Mindful Reset</span>

  <div class="bar center" style="top:1013px;">NOTES AND PLANS TO AVOID TRIGGERS</div>
  <div class="write-line" style="left:124px;top:1067px;width:651px;"></div>
  <div class="write-line" style="left:124px;top:1091px;width:651px;"></div>
  <div class="write-line" style="left:124px;top:1114px;width:651px;"></div>
</div>
</body>
</html>
```